Shaping Lattice Engineering

We need to design the look and feel for an innovation company with software products for solving complex IT problems following socio-technical theory thinking. The company is heavy in designing of complex systems (like an architect shop). The new design will form the foundation of our brand moving forward. We will approach software projects as if one is building a skyscraper or a bridge. We want to humanize technology and not the other way around. Our target groups will be healthcare and the environment. We will be able to take complex problems and turn them into amazing IT solutions that improve the quality of life for people.

Here are more fragments of ideas that can help:
===============

Motivation

The technology described in the application, coincides with “Steer-Via-Pulse” concept of Lorne Vistrup, which suggests managing a business by managing an informational representation of it : Lorne had the following vision:

"Imagine an enterprise design model that defines the behavior of an entire business. Imagine making this model a part of the corporate informational infrastructure, implementing it on technology that connects all relevant sources and users of information and affords maximum sharing among all parts of the firm. Managers could respond to the read-outs appearing on the console, modifying the flight plan en route based on changes in external conditions, monitoring the performance of delegated responsibilities, sending coordinated directions to subsidiary functions, and experiencing exhilaration upon their execution. It constitutes institutional memory and intelligence, which augment management's ability to run the business”.

This product does what Mr. Vistrup envisioned.

The Objective

QTV offers software products for the specification, construction, assembly, and ongoing management of a digital representation that is an exact mirror image of an enterprise. The main idea is the capability of managing the enterprise by managing an information technology representation of it through software. The idea is to manage the enterprise as a total system involving all aspects of operations. That makes the enterprise and all its information technology representation is inseparable. The implication is that the management of change at the business and IT infrastructure levels are unified. For example, by reconfiguring the information representation of the enterprise one can change business performance. By changing the configuration of the business representation one can actually change the organization’s ability to respond to internal and external events. Management leadership can act with the aid of technology to better respond and improve their ability to guide the organization. The knowledge management feature of the digital representation of the enterprise enables managers to monitor the impact of change and therefore help management assess risk and determine whether mitigating responses are necessary.

The technology and product defines a new approach for the design, implementation, and ongoing execution of software systems that are truly business-like rather than applications and workflows.

Software

```html
<!DOCTYPE html>
<html lang="en">
<head>
<meta charset="utf-8">
<title>IT Software — Shaping Lattice Engineering</title>
<link rel="stylesheet" href="https://fonts.googleapis.com/css2?family=Oswald:wght@300;400&family=Roboto:wght@400;700&display=swap">
<style>
:root{
  --coral:#f06b5a;
  --coral-dark:#e05a49;
  --ink:#2b2829;
  --charcoal:#3b3738;
  --charcoal-deep:#2e2b2c;
  --paper:#efefef;
  --mist:#dedede;
  --white:#ffffff;
  --muted:#6c6c6c;
  --heading:'Oswald', sans-serif;
  --body:'Roboto', sans-serif;
}
*{box-sizing:border-box;margin:0;padding:0}
html,body{width:1200px;height:3077px;overflow:hidden}
body{font-family:var(--body);color:var(--ink);background:var(--paper);position:relative}
section,header,footer,nav{position:relative}
.wrap{width:850px;margin:0 auto;position:relative}

/* top strip + nav */
.top-strip{height:34px;background:var(--charcoal-deep)}
.top-strip .wrap{display:flex;justify-content:flex-end;align-items:center;height:34px;gap:8px;color:#ddd;font-size:14px}
.top-strip svg{width:14px;height:14px}
.site-nav{height:76px;background:rgba(40,37,38,.92);z-index:2}
.site-nav .wrap{display:flex;justify-content:space-between;align-items:stretch;height:76px;width:880px}
.brand{color:var(--white);font-family:var(--body);font-size:30px;font-weight:400;display:flex;align-items:center;letter-spacing:.5px}
.menu{display:flex;list-style:none}
.menu li{display:flex;align-items:center;padding:0 20px;color:#e6e6e6;font-size:13px;border-left:1px solid rgba(255,255,255,.08)}
.menu li.active{background:var(--coral);color:var(--white)}

/* hero */
.hero{height:523px;background:linear-gradient(100deg,#bdbdbd 0%,#a9a9a9 45%,#6f6f6f 70%,#3e3e3e 100%);overflow:hidden}
.hero-art{position:absolute;inset:0}
.hero .wrap{padding-top:50px}
.hero-title{font-family:var(--body);font-weight:700;font-size:46px;line-height:1.15;color:#2a2a2a;width:520px}
.hero-tag{display:inline-block;margin-top:22px;background:var(--coral);color:var(--white);font-size:17px;padding:8px 16px}
.slider-arrows{position:absolute;right:180px;bottom:8px;display:flex;gap:4px}
.slider-arrows span{width:32px;height:32px;background:var(--coral);display:flex;align-items:center;justify-content:center}
.slider-arrows svg{width:12px;height:12px}

/* welcome */
.welcome{height:257px;background:var(--coral);color:var(--white);overflow:hidden}
.welcome .wrap{padding-top:22px}
.section-title{font-family:var(--heading);font-weight:300;font-size:50px;line-height:1.1;text-transform:uppercase}
.welcome p{font-size:19px;line-height:1.3;margin-top:14px}

/* services */
.services{height:512px;background:var(--paper);overflow:hidden}
.services .wrap{padding-top:30px}
.services .section-title{color:var(--ink)}
.lead{font-size:15px;line-height:1.45;margin-top:20px;color:#333}
.service-grid{display:flex;justify-content:space-between;margin-top:42px}
.service{width:260px}
.service-media{height:180px;position:relative}
.service-media .art{position:absolute;inset:0}
.service-caption{position:absolute;left:0;right:0;bottom:0;height:34px;background:rgba(35,33,34,.92);color:var(--white);font-weight:700;font-size:16px;display:flex;align-items:center;justify-content:center}
.service p{font-size:11px;line-height:1.5;color:var(--muted);text-align:center;margin-top:10px;padding:0 14px}

/* blog */
.blog{height:378px;background:var(--charcoal);color:#e8e8e8;overflow:hidden}
.blog .wrap{padding-top:28px}
.blog .section-title{color:var(--coral)}
.post-grid{display:flex;justify-content:space-between;margin-top:30px}
.post{width:260px;display:flex;flex-direction:column}
.post-body{display:flex;gap:12px}
.post-body i{flex:none;width:12px;height:12px;background:var(--coral);margin-top:4px}
.post-body p{font-size:12.5px;line-height:1.45}
.post-meta{display:flex;gap:10px;margin-top:22px;padding-left:24px}
.post-meta span{background:var(--coral);color:var(--white);font-size:10px;padding:7px 12px;display:flex;align-items:center;gap:5px}
.post-meta svg{width:9px;height:9px}

/* team */
.team{height:818px;background:var(--paper);overflow:hidden}
.team .wrap{padding-top:34px}
.team .lead{margin-top:8px}
.member-list{margin-left:92px;margin-top:40px;display:flex;flex-direction:column;gap:20px}
.member{display:flex;height:192px;background:var(--charcoal);color:#ddd}
.member-photo{width:192px;flex:none}
.member-info{padding:20px 22px 14px;display:flex;flex-direction:column;flex:1}
.member-info h3{color:var(--coral);font-size:22px;font-weight:700}
.member-info p{font-size:12.5px;line-height:1.45;margin-top:12px}
.member-info .more{margin-top:auto;align-self:flex-end;font-size:12px;color:var(--white)}

/* testimonial */
.testimonial{height:280px;background:var(--mist);overflow:hidden}
.testimonial .wrap{padding-top:30px}
.testimonial .section-title{color:var(--ink);font-size:46px}
.quote{display:flex;align-items:center;margin-top:30px;margin-left:-10px;gap:22px}
.quote-photo{width:88px;height:88px;border-radius:50%;border:4px solid var(--coral);flex:none;background:linear-gradient(135deg,#d9c3b3,#8b6f60)}
.quote-text{position:relative;padding:4px 46px 0;font-size:13px;line-height:1.5;color:#333;flex:1}
.quote-text .mark{position:absolute;font-family:Georgia,serif;font-size:60px;line-height:1;color:var(--ink)}
.quote-text .open{left:0;top:-12px}
.quote-text .close{right:0;bottom:-30px}
.quote-text cite{display:block;text-align:right;color:var(--coral);font-style:italic;font-size:12px;margin-top:8px;padding-right:50px}

/* footer */
.footer-nav{height:46px;background:var(--coral)}
.footer-nav ul{list-style:none;display:flex;justify-content:center;gap:46px;height:46px;align-items:center;color:var(--white);font-size:13px;font-weight:700}
.site-footer{height:151px;background:var(--charcoal-deep);color:#ccc;text-align:center;padding-top:26px;font-size:13px}
.social{display:flex;justify-content:center;gap:8px;margin-top:12px}
.social span{width:24px;height:24px;background:#5a5657}
.site-footer small{display:block;margin-top:14px;font-size:12px}
</style>
</head>
<body>

<header>
  <div class="top-strip">
    <div class="wrap">
      <svg viewBox="0 0 16 16" aria-hidden="true"><path d="M3 1l3 3-2 2c1 2 3 4 5 5l2-2 3 3-2 2C7 14 2 9 1 3z" fill="#f06b5a"/></svg>
      <span>01234-567-8901</span>
    </div>
  </div>
  <nav class="site-nav">
    <div class="wrap">
      <div class="brand">IT SOFTWARE</div>
      <ul class="menu">
        <li class="active">Home</li>
        <li>What we do</li>
        <li>News blog</li>
        <li>Software</li>
        <li>Our Team</li>
        <li>Contact Us</li>
      </ul>
    </div>
  </nav>
</header>

<section class="hero">
  <div class="hero-art" role="img" aria-label="Photo of a businessman in a suit using a tablet, with scattered letters on a grey wall"></div>
  <div class="wrap">
    <h1 class="hero-title">Lorem ipsum dolor sit amet, consectetur</h1>
    <div class="hero-tag">Lorem ipsum dolor sit amet, consectetur adipiscing elit</div>
  </div>
  <div class="slider-arrows">
    <span><svg viewBox="0 0 12 12"><path d="M8 1L3 6l5 5" stroke="#fff" stroke-width="2" fill="none"/></svg></span>
    <span><svg viewBox="0 0 12 12"><path d="M4 1l5 5-5 5" stroke="#fff" stroke-width="2" fill="none"/></svg></span>
  </div>
</section>

<section class="welcome">
  <div class="wrap">
    <h2 class="section-title">Welcome</h2>
    <p>Lorem ipsum dolor sit amet, consectetur adipisicing elit, sed do eiusmod tempor incididunt ut labore et dolore magna aliqua. Ut enim ad minim veniam, quis nostrud exercitation ullamco laboris nisi ut aliquip ex ea commodo consequat. Duis aute irure dolor in reprehenderit in voluptate velit esse cillum dolore eu fugiat nulla pariatur.</p>
  </div>
</section>

<section class="services">
  <div class="wrap">
    <h2 class="section-title">What we do</h2>
    <p class="lead">Lorem ipsum dolor sit amet, consectetur adipisicing elit, sed do eiusmod tempor incididunt ut labore et dolore magna aliqua. Ut enim ad minim veniam, quis nostrud exercitation ullamco laboris nisi ut aliquip ex ea commodo consequat.</p>
    <div class="service-grid">
      <article class="service">
        <div class="service-media">
          <div class="art" role="img" aria-label="Photo of a city skyline at dusk" style="background:linear-gradient(180deg,#2f5fa8,#c9763f)"></div>
          <div class="service-caption">Lorem ipsum dolor</div>
        </div>
        <p>Sed ut perspiciatis unde omnis iste natus error sit voluptatem accusantium doloremque laudantium totam rem aperiam</p>
      </article>
      <article class="service">
        <div class="service-media">
          <div class="art" role="img" aria-label="Photo of a hand touching a glowing digital screen" style="background:linear-gradient(160deg,#e9f2fa,#6fa3d6)"></div>
          <div class="service-caption">Lorem ipsum dolor</div>
        </div>
        <p>Nemo enim ipsam voluptatem quia voluptas sit aspernatur aut odit aut fugit sed quia consequuntur magni</p>
      </article>
      <article class="service">
        <div class="service-media">
          <div class="art" role="img" aria-label="Photo of a business team standing together" style="background:linear-gradient(180deg,#f4f4f4,#4a4a55)"></div>
          <div class="service-caption">Lorem ipsum dolor</div>
        </div>
        <p>Neque porro quisquam est qui dolorem ipsum quia dolor sit amet consectetur adipisci velit sed quia</p>
      </article>
    </div>
  </div>
</section>

<section class="blog">
  <div class="wrap">
    <h2 class="section-title">New Blog</h2>
    <div class="post-grid">
      <article class="post">
        <div class="post-body"><i></i><p>Lorem ipsum dolor sit amet, consectetur adipisicing elit, sed do eiusmod tempor incididunt ut labore et dolore magna aliqua. Ut enim ad minim veniam, quis nostrud exercitation ullamco laboris nisi ut aliquip ex ea commodo consequat.</p></div>
        <div class="post-meta">
          <span><svg viewBox="0 0 10 10"><circle cx="5" cy="3" r="2.5" fill="#fff"/><path d="M0 10c0-3 2-4 5-4s5 1 5 4z" fill="#fff"/></svg>Posted by Guru</span>
          <span><svg viewBox="0 0 10 10"><path d="M0 0h10v7H4l-3 3V7H0z" fill="#fff"/></svg>Comments</span>
        </div>
      </article>
      <article class="post">
        <div class="post-body"><i></i><p>Lorem ipsum dolor sit amet, consectetur adipisicing elit, sed do eiusmod tempor incididunt ut labore et dolore magna aliqua. Ut enim ad minim veniam, quis nostrud exercitation ullamco laboris nisi ut aliquip ex ea commodo consequat.</p></div>
        <div class="post-meta">
          <span><svg viewBox="0 0 10 10"><circle cx="5" cy="3" r="2.5" fill="#fff"/><path d="M0 10c0-3 2-4 5-4s5 1 5 4z" fill="#fff"/></svg>Posted by Guru</span>
          <span><svg viewBox="0 0 10 10"><path d="M0 0h10v7H4l-3 3V7H0z" fill="#fff"/></svg>Comments</span>
        </div>
      </article>
      <article class="post">
        <div class="post-body"><i></i><p>Lorem ipsum dolor sit amet, consectetur adipisicing elit, sed do eiusmod tempor incididunt ut labore et dolore magna aliqua. Ut enim ad minim veniam, quis nostrud exercitation ullamco laboris nisi ut aliquip ex ea commodo consequat.</p></div>
        <div class="post-meta">
          <span><svg viewBox="0 0 10 10"><circle cx="5" cy="3" r="2.5" fill="#fff"/><path d="M0 10c0-3 2-4 5-4s5 1 5 4z" fill="#fff"/></svg>Posted by Guru</span>
          <span><svg viewBox="0 0 10 10"><path d="M0 0h10v7H4l-3 3V7H0z" fill="#fff"/></svg>Comments</span>
        </div>
      </article>
    </div>
  </div>
</section>

<section class="team">
  <div class="wrap">
    <h2 class="section-title">Our Team</h2>
    <p class="lead">Lorem ipsum dolor sit amet, consectetur adipisicing elit, sed do eiusmod tempor incididunt ut labore et dolore.</p>
    <div class="member-list">
      <article class="member">
        <div class="member-photo" role="img" aria-label="Portrait photo of a team member in a suit" style="background:linear-gradient(160deg,#e8e8e8,#8a8a8a)"></div>
        <div class="member-info">
          <h3>Lorem ipsum dolor</h3>
          <p>Lorem ipsum dolor sit amet, consectetur adipisicing elit, sed do eiusmod tempor incididunt ut labore et dolore magna aliqua. Ut enim ad minim veniam, quis nostrud exercitation ullamco laboris nisi ut aliquip ex ea commodo consequat.</p>
          <span class="more">Read more</span>
        </div>
      </article>
      <article class="member">
        <div class="member-photo" role="img" aria-label="Portrait photo of a smiling team member in a suit" style="background:linear-gradient(160deg,#f0f0f0,#7d7f86)"></div>
        <div class="member-info">
          <h3>Lorem ipsum dolor</h3>
          <p>Lorem ipsum dolor sit amet, consectetur adipisicing elit, sed do eiusmod tempor incididunt ut labore et dolore magna aliqua. Ut enim ad minim veniam, quis nostrud exercitation ullamco laboris nisi ut aliquip ex ea commodo consequat.</p>
          <span class="more">Read more</span>
        </div>
      </article>
      <article class="member">
        <div class="member-photo" role="img" aria-label="Portrait photo of a smiling female team member" style="background:linear-gradient(160deg,#f2ece8,#8c6f62)"></div>
        <div class="member-info">
          <h3>Lorem ipsum dolor</h3>
          <p>Lorem ipsum dolor sit amet, consectetur adipisicing elit, sed do eiusmod tempor incididunt ut labore et dolore magna aliqua. Ut enim ad minim veniam, quis nostrud exercitation ullamco laboris nisi ut aliquip ex ea commodo consequat.</p>
          <span class="more">Read more</span>
        </div>
      </article>
    </div>
  </div>
</section>

<section class="testimonial">
  <div class="wrap">
    <h2 class="section-title">Client Testimonial</h2>
    <div class="quote">
      <div class="quote-photo" role="img" aria-label="Round portrait photo of the client"></div>
      <blockquote class="quote-text">
        <span class="mark open">&ldquo;</span>
        Lorem ipsum dolor sit amet, consectetur adipisicing elit, sed do eiusmod tempor incididunt ut labore et dolore magna aliqua. Ut enim ad minim veniam, quis nostrud exercitation ullamco laboris nisi ut aliquip ex ea commodo consequat.
        <span class="mark close">&rdquo;</span>
        <cite>-Tomas</cite>
      </blockquote>
    </div>
  </div>
</section>

<nav class="footer-nav">
  <ul>
    <li>Home</li>
    <li>What we do</li>
    <li>News blog</li>
    <li>Software</li>
    <li>Our Team</li>
    <li>Contact Us</li>
  </ul>
</nav>

<footer class="site-footer">
  <div>Follow Us</div>
  <div class="social"><span></span><span></span><span></span><span></span></div>
  <small>Privacy | Copyright</small>
</footer>

</body>
</html>
```